Mabel's Fitness Business Cards

I would like my business cards to look expensive and sophisticated using my logo and the information below.

FRONT
Mabel’s Fitness logo

Tag line Become your happiest, healthiest and strongest self

Mabel Quint Harlow
Personal Trainer

e. mabel@mabelsfitstudio.example

t. 0781530462

w. www.mabelsfitstudio.example

```html
<!DOCTYPE html>
<html lang="en">
<head>
<meta charset="utf-8">
<title>Mabel's Fitness Business Cards</title>
<link rel="stylesheet" href="https://fonts.googleapis.com/css2?family=Josefin+Sans:wght@300;400;600&family=Open+Sans:wght@400&display=swap">
<style>
  :root {
    --backdrop: #141414;
    --card-black: #0c0c0d;
    --card-white: #f7f7f6;
    --taupe: #aaa19e;
    --teal: #7ec0c9;
    --bar-grey: #55514f;
    --text-white: #f2f2f2;
    --faint: #dcdcdb;
  }
  * { box-sizing: border-box; margin: 0; padding: 0; }
  html, body { width: 1200px; height: 864px; overflow: hidden; }
  body {
    background: radial-gradient(ellipse at 50% 45%, #232323 0%, var(--backdrop) 70%);
    font-family: "Josefin Sans", sans-serif;
    display: flex;
    flex-direction: column;
    align-items: center;
    justify-content: center;
    gap: 48px;
  }
  .card {
    position: relative;
    width: 640px;
    height: 360px;
    overflow: hidden;
    box-shadow: 0 10px 30px rgba(0,0,0,.6);
  }

  /* Logo side */
  .card--brand {
    background:
      linear-gradient(100deg, var(--taupe) 0 9%, transparent 9%),
      linear-gradient(160deg, #1b1b1c 0%, var(--card-black) 60%);
  }
  .brand-disc {
    position: absolute;
    left: 8px; top: -8px;
    width: 376px; height: 376px;
    border-radius: 50%;
    background: var(--card-white);
    border: 11px solid var(--teal);
    display: flex; align-items: center; justify-content: center;
  }
  .brand-disc__name {
    font-weight: 300;
    font-size: 30px;
    letter-spacing: 4px;
    color: var(--teal);
    text-transform: uppercase;
  }
  .wordmark {
    position: absolute;
    left: 396px; top: 128px;
    color: var(--teal);
    font-weight: 300;
    text-transform: uppercase;
  }
  .wordmark__line1 { font-size: 34px; letter-spacing: 3px; display: block; }
  .wordmark__line2 { font-size: 20px; letter-spacing: 12px; display: block; margin-top: 2px; }
  .wordmark__bar {
    position: absolute;
    left: 388px; top: 208px;
    width: 220px; height: 5px;
    background: var(--bar-grey);
  }
  .tagline {
    position: absolute;
    left: 388px; top: 236px;
    width: 230px;
    text-align: center;
    color: var(--text-white);
    font-size: 11px;
    letter-spacing: 2px;
    line-height: 1.7;
    text-transform: uppercase;
  }

  /* Contact side */
  .card--contact {
    background:
      linear-gradient(100deg, transparent 91%, var(--taupe) 91%),
      var(--card-white);
  }
  .faint-name {
    position: absolute;
    left: 30px; top: 150px;
    font-size: 34px;
    font-weight: 300;
    letter-spacing: 4px;
    color: var(--faint);
    text-transform: uppercase;
  }
  .contact-disc {
    position: absolute;
    left: 276px; top: -14px;
    width: 392px; height: 392px;
    border-radius: 50%;
    background: radial-gradient(circle at 40% 30%, #1e1e1f 0%, var(--card-black) 60%);
    border: 8px solid var(--teal);
  }
  .person {
    position: absolute;
    left: 352px; top: 110px;
  }
  .person__name {
    color: var(--teal);
    font-size: 19px;
    font-weight: 400;
    letter-spacing: 1.5px;
    text-transform: uppercase;
  }
  .person__role {
    color: var(--text-white);
    font-family: "Open Sans", sans-serif;
    font-size: 13px;
    margin-top: 2px;
  }
  .person__bar {
    width: 232px; height: 5px;
    background: var(--bar-grey);
    margin-top: 10px;
  }
  .contacts {
    list-style: none;
    position: absolute;
    left: 356px; top: 200px;
    color: var(--text-white);
    font-size: 14px;
    letter-spacing: .6px;
  }
  .contacts li { display: flex; align-items: center; gap: 8px; margin-bottom: 7px; }
  .contacts svg { width: 15px; height: 15px; flex: none; }
  .contacts .web { font-weight: 600; }
</style>
</head>
<body>

  <section class="card card--brand">
    <div class="brand-disc"><span class="brand-disc__name">Mabel’s Fitness</span></div>
    <div class="wordmark">
      <span class="wordmark__line1">Mabel’s</span>
      <span class="wordmark__line2">Fitness</span>
    </div>
    <div class="wordmark__bar"></div>
    <p class="tagline">Become your happiest, healthiest and strongest self</p>
  </section>

  <section class="card card--contact">
    <div class="faint-name">Mabel’s Fitness</div>
    <div class="contact-disc"></div>
    <div class="person">
      <h1 class="person__name">Mabel Quint Harlow</h1>
      <p class="person__role">Personal Trainer</p>
      <div class="person__bar"></div>
    </div>
    <ul class="contacts">
      <li>
        <svg viewBox="0 0 16 16" aria-hidden="true"><circle cx="8" cy="8" r="7" fill="none" stroke="#7ec0c9" stroke-width="1.4"/><path d="M5.5 4.5l1.3 0 .6 1.8-.9.7c.5 1 1.3 1.8 2.3 2.3l.7-.9 1.8.6v1.3c-3.2.3-6.1-2.6-5.8-5.8z" fill="#7ec0c9"/></svg>
        078 1530 462
      </li>
      <li>
        <svg viewBox="0 0 16 16" aria-hidden="true"><circle cx="8" cy="8" r="7" fill="none" stroke="#7ec0c9" stroke-width="1.4"/><rect x="4.3" y="5.5" width="7.4" height="5" fill="none" stroke="#7ec0c9" stroke-width="1"/><path d="M4.3 5.5L8 8.3l3.7-2.8" fill="none" stroke="#7ec0c9" stroke-width="1"/></svg>
        mabel@mabelsfitstudio.example
      </li>
      <li>
        <svg viewBox="0 0 16 16" aria-hidden="true"><circle cx="8" cy="8" r="7" fill="none" stroke="#7ec0c9" stroke-width="1.4"/><circle cx="8" cy="8" r="3.6" fill="none" stroke="#7ec0c9" stroke-width="1"/><path d="M4.4 8h7.2M8 4.4c-1.6 2.2-1.6 5 0 7.2M8 4.4c1.6 2.2 1.6 5 0 7.2" fill="none" stroke="#7ec0c9" stroke-width=".9"/></svg>
        <span class="web">www.mabelsfitstudio.example</span>
      </li>
    </ul>
  </section>

</body>
</html>
```